Mavro Scrub - Contact/Landing Page

I need a landing page which will essentially be the page that customers will go to from the 'website' link on GMB listing. It will provide a short overview of services which need to be selectable. a little further down can capture some contact details followed by a large Submit Now button etc...

I have some icon/logo's that can be utilised at the bottom of the page as industry type references.

Target Market(s)

End of Lease Cleaning Services

Industry/Entity Type

Cleaning Service

Colors

Designer to choose colors to be used in the design.

Requirements
Must have
• As per description
Should not have
• Colours to match my website mavroscrub.com.au

```html
<!DOCTYPE html>
<html lang="en">
<head>
<meta charset="utf-8">
<title>Mavro Scrub – End Of Lease Services</title>
<link href="https://fonts.googleapis.com/css2?family=Alfa+Slab+One&family=Arvo:wght@700&family=Oswald:wght@500;600&family=Open+Sans:ital,wght@0,400;0,600;1,400&display=swap" rel="stylesheet">
<style>
:root{
  --hero-blue:#3d97c9;
  --hero-deep:#2a6f9e;
  --accent:#27b6e8;
  --line-blue:#2a8fd0;
  --ink:#151515;
  --body:#333;
  --panel:#e6e9ee;
  --white:#fff;
  --link:#1f6fc0;
  --email:#d21d2b;
  --footer:#555;
}
*{box-sizing:border-box;margin:0;padding:0}
html,body{width:733px;height:1200px;overflow:hidden;background:var(--white)}
body{position:relative;font-family:"Open Sans",sans-serif;color:var(--body)}
.abs{position:absolute}

.hero{left:0;top:0;width:733px;height:524px;background:linear-gradient(180deg,var(--hero-deep) 0%,#3585b8 45%,var(--hero-blue) 100%)}
.hero-backdrop{left:0;top:0;width:733px;height:524px;background:linear-gradient(180deg,rgba(120,170,210,.25) 0%,rgba(120,170,210,0) 55%)}
.hero-ring{left:217px;top:58px;width:298px;height:298px;border-radius:50%;background:var(--accent);border:4px solid var(--white)}
.hero-photo{left:228px;top:69px;width:276px;height:276px;border-radius:50%;background:radial-gradient(circle at 55% 55%,#a9693a 0%,#c9b49a 30%,#e4dccd 70%)}
.thumb{width:98px;height:98px;border-radius:50%;border:4px solid #1d2430}
.thumb-a{left:188px;top:214px;background:radial-gradient(circle,#b08a62,#dcdcd8)}
.thumb-b{left:433px;top:215px;background:radial-gradient(circle,#8a3b1e,#e0dcd6)}
.thumb-c{left:317px;top:274px;background:linear-gradient(135deg,#f4f4f4,#c7ccd3 60%,#3b5f94)}
.brand-tag{left:310px;top:0;width:113px;height:137px}
.brand-name{left:310px;top:48px;width:113px;text-align:center;font-family:"Oswald",sans-serif;font-weight:600;font-size:21px;line-height:24px;color:var(--accent)}
.hero-title{left:0;top:133px;width:733px;text-align:center;font-family:"Arvo",serif;font-weight:700;font-size:21px;color:var(--white);text-shadow:0 1px 3px rgba(0,0,0,.45);letter-spacing:.3px}
.hero-title .sep{display:inline-block;width:1px;height:18px;background:var(--white);margin:0 8px;vertical-align:-2px}
.section-title{left:0;top:394px;width:733px;text-align:center;font-family:"Alfa Slab One",serif;font-weight:400;font-size:28px;line-height:29px;color:var(--white)}

.card{width:173px;height:300px}
.card-outline{left:0;top:39px;width:173px;height:215px;border:1.5px solid var(--line-blue);border-radius:84px 84px 86px 86px/70px 70px 120px 120px;background:var(--white)}
.card svg{position:absolute;left:0;top:0}
.card-icon{left:64px;top:56px;width:45px;height:45px;border-radius:50%;background:var(--white)}
.card-title{left:0;top:106px;width:173px;text-align:center;font-family:"Oswald",sans-serif;font-weight:600;font-size:21px;color:var(--ink);letter-spacing:.3px}
.card-rule{left:28px;top:139px;width:117px;height:1px;background:#777}
.card-spark{left:140px;top:98px;font-size:10px;color:#333}
.card-text{left:10px;top:150px;width:153px;text-align:center;font-size:10.5px;line-height:13px;color:var(--body)}
.card-text a{color:var(--link);text-decoration:none}
.card-select{left:0;top:205px;width:173px;text-align:center;font-size:9.5px;font-weight:600;color:var(--body)}
.box{display:inline-block;width:8px;height:8px;border:1px solid #333;vertical-align:-1px;margin-left:3px}
.box.on{border-color:var(--line-blue);position:relative}
.box.on::after{content:"";position:absolute;left:2px;top:0;width:2px;height:4px;border:solid var(--line-blue);border-width:0 1px 1px 0;transform:rotate(45deg)}

.contact{left:0;top:770px;width:733px;height:271px;background:var(--panel)}
.contact-photo{left:341px;top:770px;width:392px;height:271px;background:radial-gradient(ellipse 90px 130px at 55% 65%,rgba(120,150,200,.55),rgba(120,150,200,0)),linear-gradient(90deg,var(--panel) 0%,#dedfe0 25%,#d8d2c8 45%,#e6e8ea 70%,#eff0f2 100%)}
.contact-accent{left:628px;top:895px;width:105px;height:36px;background:var(--accent)}
.contact-title{left:96px;top:800px;font-family:"Oswald",sans-serif;font-weight:600;font-size:31px;color:var(--ink);letter-spacing:.5px}
.field{background:var(--white);border:1px solid #cfd3d8;font-size:8px;color:#444;padding:6px 8px}
.email{left:96px;top:961px;width:238px;text-align:center;font-style:italic;font-size:10.5px;color:var(--email)}
.submit{left:96px;top:978px;width:238px;height:26px;background:var(--accent);color:var(--white);font-family:"Oswald",sans-serif;font-weight:500;font-size:15px;letter-spacing:2px;text-align:center;line-height:26px}

.badge{top:1088px;width:128px;height:52px;border:1px solid #ddd;background:var(--white);box-shadow:0 0 2px rgba(0,0,0,.08);display:flex;align-items:center;justify-content:center}
.badge span{display:block;width:80px;height:30px;border-radius:3px}
.footer{left:0;top:1179px;width:733px;height:21px;background:var(--footer);color:#eee;font-size:8px;text-align:center;line-height:21px}
</style>
</head>
<body>

<section class="abs hero" aria-label="Hero">
  <div class="abs hero-backdrop" role="img" aria-label="Blurred photo of a cleaner mopping a floor"></div>
  <div class="abs hero-ring"></div>
  <div class="abs hero-photo" role="img" aria-label="Close-up photo of a dead cockroach on the floor"></div>
  <div class="abs thumb thumb-a" role="img" aria-label="Photo of ants on wood"></div>
  <div class="abs thumb thumb-b" role="img" aria-label="Photo of cockroaches"></div>
  <div class="abs thumb thumb-c" role="img" aria-label="Photo of a technician spraying a wall"></div>
  <svg class="abs brand-tag" viewBox="0 0 113 137" aria-hidden="true">
    <polygon points="0,0 113,0 113,115 56.5,136 0,115" fill="#fff"/>
    <polyline points="0,115 56.5,136 113,115" fill="none" stroke="#2d2d2d" stroke-width="3"/>
  </svg>
  <div class="abs brand-name">MAVRO<br>SCRUB</div>
  <h1 class="abs hero-title">End Of Lease Cleaning<span class="sep"></span>Licensed Pest Control</h1>
  <h2 class="abs section-title">End Of Lease<br>Services</h2>
</section>

<div class="abs card" style="left:96px;top:480px">
  <div class="abs card-outline"></div>
  <svg width="173" height="80" viewBox="0 0 173 80" role="img" aria-label="Photo of a floor being mopped">
    <polygon points="86.5,0 150.5,44 132.5,44 132.5,74 40.5,74 40.5,44 22.5,44" fill="#4a4f57"/>
  </svg>
  <div class="abs card-icon"></div>
  <svg class="abs" style="left:76px;top:62px" width="21" height="21" viewBox="0 0 21 21" fill="none" stroke="#222" stroke-width="1"><path d="M3 19h15M5 19l2-8h7l2 8M10 11V3M13 6h4v5"/></svg>
  <div class="abs card-spark">✧</div>
  <div class="abs card-title">CLEANING</div>
  <div class="abs card-rule"></div>
  <p class="abs card-text">All interior cleaning carried out <a>Property Management</a> Requirements</p>
  <div class="abs card-select">Select<span class="box on"></span></div>
</div>

<div class="abs card" style="left:280px;top:480px">
  <div class="abs card-outline"></div>
  <svg width="173" height="80" viewBox="0 0 173 80" role="img" aria-label="Photo of a carpet steam cleaner">
    <polygon points="86.5,0 150.5,44 132.5,44 132.5,74 40.5,74 40.5,44 22.5,44" fill="#55524e"/>
  </svg>
  <div class="abs card-icon"></div>
  <svg class="abs" style="left:76px;top:62px" width="21" height="21" viewBox="0 0 21 21" fill="none" stroke="#222" stroke-width="1"><rect x="3" y="9" width="6" height="10" rx="1"/><path d="M6 9V3h5v4M13 19V7a3 3 0 0 1 5 0v12M11 19h9"/></svg>
  <div class="abs card-spark">✧</div>
  <div class="abs card-title">CARPET CLEANING</div>
  <div class="abs card-rule"></div>
  <p class="abs card-text" style="top:144px">Carpet steam cleaning to Australian<br>standard as 3733 : 1995</p>
  <div class="abs card-select">Select<span class="box"></span></div>
</div>

<div class="abs card" style="left:464px;top:480px">
  <div class="abs card-outline"></div>
  <svg width="173" height="80" viewBox="0 0 173 80" role="img" aria-label="Photo of a pest control sprayer">
    <polygon points="86.5,0 150.5,44 132.5,44 132.5,74 40.5,74 40.5,44 22.5,44" fill="#3e5476"/>
  </svg>
  <div class="abs card-icon"></div>
  <svg class="abs" style="left:76px;top:62px" width="21" height="21" viewBox="0 0 21 21" fill="none" stroke="#222" stroke-width="1"><ellipse cx="9" cy="11" rx="4" ry="6"/><path d="M7 4l-2-2M11 4l2-2M5 9H2M5 13H2M13 9h3M13 13h3"/><rect x="13" y="12" width="5" height="7" rx="1"/></svg>
  <div class="abs card-spark">✧</div>
  <div class="abs card-title">PEST CONTROL</div>
  <div class="abs card-rule"></div>
  <p class="abs card-text" style="top:144px">Mandatory requirement<br>for pets on premises</p>
  <div class="abs card-select">Select<span class="box"></span></div>
</div>

<section aria-label="Contact">
  <div class="abs contact"></div>
  <div class="abs contact-photo" role="img" aria-label="Photo of a smiling pest control technician with a sprayer"></div>
  <div class="abs contact-accent"></div>
  <h2 class="abs contact-title">CONTACT US</h2>
  <div class="abs field" style="left:96px;top:841px;width:117px;height:23px">First Name :</div>
  <div class="abs field" style="left:218px;top:841px;width:116px;height:23px">Last Name :</div>
  <div class="abs field" style="left:96px;top:868px;width:117px;height:23px">Email :</div>
  <div class="abs field" style="left:218px;top:868px;width:116px;height:23px">Ph :</div>
  <div class="abs field" style="left:96px;top:895px;width:238px;height:63px">Message :</div>
  <div class="abs email">infomavroscrub.com.au</div>
  <div class="abs submit">SUBMIT</div>
</section>

<div class="abs badge" style="left:96px"><span style="background:#222"></span></div>
<div class="abs badge" style="left:234px"><span style="background:#1f3a8a;width:54px"></span></div>
<div class="abs badge" style="left:372px"><span style="background:linear-gradient(90deg,#3a4aa0,#c8202f)"></span></div>
<div class="abs badge" style="left:509px"><span style="background:#8dbb3a;width:100px;height:28px;border-radius:0"></span></div>

<footer class="abs footer">Copyright©2021 mavro scrub. All Rights Reserved.</footer>
</body>
</html>
```